" O INSTITUTO TERAVUNDA foi idealizado a partir de um ideal de auxílio humanitário a famílias (com algum idoso) com condições de sobrevivência comprometidas devido a problemas de doença, seja ela física; psicológica ou mesmo social. “ Teravunda” significa “dono da coragem” e, apesar de seu principal mantenedor ser uma casa de culto de matriz africana (Dasilore Mitaku Fenjo Arupe),o Centro Cultural visa atender a famílias com idosos que estejam desestruturadas, devido a algum tipo de doença, indiferente a visão política, religiosa e/ou cultural. Acreditamos que o idoso incluído num contexto familiar, ou mesmo num asilo, não deve ser culpado por qualquer atitude de sua juventude. Quem de nós, em idade de produção e escolhas pode garantir estar tomando decisões acertadas para seu futuro? Normalmente são as doenças que comprometem o bem estar social: vícios em bebidas e/ou drogas; doenças patológicas e/ou psicológicas ou mesmo “doenças sociais” desestruturam as relações interpessoais afastando os idosos da realidade. "

```html
<!DOCTYPE html>
<html lang="pt-BR">
<head>
<meta charset="UTF-8">
<title>Instituto Teravunda — Depoimentos</title>
<link rel="stylesheet" href="https://fonts.googleapis.com/css2?family=Roboto+Condensed:wght@700&family=Open+Sans:wght@400;700&display=swap">
<style>
  :root {
    --canvas-bg: #e9e9e9;
    --page-bg: #ffffff;
    --accent: #e8572a;
    --ink: #3a2f2a;
    --body-text: #5d5752;
    --photo-light: #efece6;
    --photo-dark: #b8aca0;
    --footer-top: #a3702f;
    --footer-bottom: #7d5226;
    --footer-text: #f7efe4;
  }
  * { margin: 0; padding: 0; box-sizing: border-box; }
  html, body {
    width: 1200px; height: 1200px; overflow: hidden;
    background: var(--canvas-bg);
  }
  .site {
    position: absolute; left: 0; top: 225px;
    width: 1200px; height: 750px;
    background: var(--page-bg);
    overflow: hidden;
  }
  .top-bar {
    position: absolute; left: 0; top: 0; width: 100%; height: 24px;
    background: var(--accent);
  }
  .testimonial-photo {
    position: absolute; left: 420px; top: 24px; right: 0; bottom: 96px;
    background:
      linear-gradient(90deg, var(--page-bg) 0%, rgba(255,255,255,0) 22%),
      linear-gradient(180deg, var(--photo-light) 0%, var(--photo-dark) 100%);
  }
  .testimonials {
    position: absolute; left: 48px; top: 70px; width: 440px;
  }
  .section-title {
    font-family: "Roboto Condensed", sans-serif;
    font-weight: 700; font-size: 44px; line-height: 1;
    color: var(--accent);
  }
  .author {
    margin-top: 38px;
    font-family: "Roboto Condensed", sans-serif;
    font-weight: 700; font-size: 34px; line-height: 1;
    color: var(--ink);
  }
  .author-city {
    font-size: 18px; color: var(--accent);
  }
  .quote {
    margin-top: 20px;
    font-family: "Open Sans", sans-serif;
    font-size: 15px; line-height: 25px;
    color: var(--body-text);
    text-align: justify;
  }
  .slider-nav {
    position: absolute; left: 48px; top: 464px;
    display: flex; gap: 14px;
  }
  .slider-nav svg { display: block; }
  .site-footer {
    position: absolute; left: 0; bottom: 0; width: 100%; height: 96px;
    background: linear-gradient(180deg, var(--footer-top) 0%, var(--footer-bottom) 100%);
    font-family: "Open Sans", sans-serif;
    font-weight: 700; font-size: 17px; letter-spacing: 3px;
    color: var(--footer-text);
  }
  .footer-link {
    position: absolute; top: 50%; transform: translateY(-50%);
    font-variant: small-caps; text-transform: lowercase;
  }
  .footer-link.message { left: 300px; }
  .footer-link.contact { left: 880px; }
</style>
</head>
<body>
  <main class="site">
    <div class="top-bar"></div>

    <div class="testimonial-photo" role="img" aria-label="Fotografia de um homem adulto sorrindo ao lado de um idoso, ambos sentados à mesa"></div>

    <section class="testimonials">
      <h1 class="section-title">Depoimentos</h1>
      <h2 class="author">Rafael Tomé, <span class="author-city">Vila Serena SP</span></h2>
      <p class="quote">Lorem ipsum dolor sit amet, consectetur adipiscing elit, sed do eiusmod tempor incididunt ut labore et dolore magna aliqua. Ut enim ad minim veniam, quis nostrud exercitation ullamco laboris nisi ut aliquip ex ea commodo consequat. Duis aute irure dolor in reprehenderit in voluptate velit esse cillum dolore eu fugiat nulla pariatur. Excepteur sint occaecat cupidatat non proident, sunt in culpa qui officia deserunt.</p>
    </section>

    <nav class="slider-nav" aria-label="Navegar depoimentos">
      <svg width="40" height="40" viewBox="0 0 40 40" aria-label="Anterior">
        <circle cx="20" cy="20" r="20" fill="var(--accent)"/>
        <path d="M23 12 L15 20 L23 28 M15 20 H29" fill="none" stroke="#fff" stroke-width="3.5" stroke-linecap="round" stroke-linejoin="round"/>
      </svg>
      <svg width="40" height="40" viewBox="0 0 40 40" aria-label="Próximo">
        <circle cx="20" cy="20" r="20" fill="var(--accent)"/>
        <path d="M17 12 L25 20 L17 28 M25 20 H11" fill="none" stroke="#fff" stroke-width="3.5" stroke-linecap="round" stroke-linejoin="round"/>
      </svg>
    </nav>

    <footer class="site-footer">
      <span class="footer-link message">Envie-nos uma mensagem</span>
      <span class="footer-link contact">Contato</span>
    </footer>
  </main>
</body>
</html>
```